Easy Design Packaging for an environmentally friendly Insect Catcher

I need a design, to go on a sticker for the front and back of my packaging. The product is a bug catcher that is easy to use, with no dangerous chemicals and the user can decide to kill or save the bug. Eventually this product will be sold in retail so the design should POP to catch a users eyes and also speak environmentally friendly because the other alternatives that are on retail shelves are chemical sprays that are harmful to the person and environment. Those bug sprays are also meant to kill the bug so this is clearly better for the environment in that sense as well.

The front design must be 4 inches wide and range from 6 to 9 inches long. The back design must be between 3.5 and 4 inches wide and no longer than the front packaging design. Preferably they should be the same size.

I made my own version that I uploaded. Its a good start but doesn't really say environmentally friendly, and doesn't pop as much as I'd like. You may use any or all of the current design, or you can make it completely different if you have a different vision. Be advised that the spider, and the stars on the logo are licensed and you may use them. If you would like to use other artwork, please feel free and I will pay for the extended license. Please let me know when you upload it that it's a licensed image.

The front design must include the name of the product, the tag line, and the 5 lines of text. You may include other phrases as well if you would like, for example, you could add something at the top in a bubble of some sort that says "Environmentally Friendly!" The actual text doesn't matter because I can change that on my own. For the copy on the back of the package, you can write whatever you want or use the text I already have written and I will add the correct text on my own later. If the font is changed to a font that doesn't come standard with Illustrator, please let me know what it is so I can download it.

If the design you have in mind needs a different logo feel free to change around the logo in any way or add the logo and I will pay for it. I can also hire you directly for the logo as well, if I choose your design.

Feel free to ask any questions and give me feedback or suggestions.
Thanks

Target Market(s)

Pretty much anyone that doesn't like bugs but maybe a little geared toward women.

Industry/Entity Type

Product

Colors

Designer to choose colors to be used in the design.

Requirements
Must have
• Please read the description for all the must haves
Nice to have
• Please read the description for all the nice to haves
Should not have
• Should not include anything that gives the idea of killing the insect, or anything that makes it look expensive, as it is a cheap product.

```html
<!DOCTYPE html>
<html lang="en">
<head>
<meta charset="utf-8">
<title>The Swift Bug Stick – Packaging Sticker</title>
<link rel="stylesheet" href="https://fonts.googleapis.com/css2?family=Fredoka:wght@600;700&family=Overlock:wght@700&family=Oswald:wght@500&display=swap">
<style>
  :root {
    --navy: #1d1a62;
    --glow: #5a2590;
    --purple: #8f2a8e;
    --green: #0e9447;
    --green-dark: #0a6f35;
    --orange: #f6a53c;
    --yellow: #fdf02a;
    --ink: #1b1420;
    --white: #ffffff;
    --bug-brown: #5b4338;
  }
  * { box-sizing: border-box; margin: 0; padding: 0; }
  html, body { width: 816px; height: 1200px; overflow: hidden; background: var(--white); }
  .sticker {
    position: relative;
    width: 816px;
    height: 1200px;
    overflow: hidden;
    background: linear-gradient(180deg, var(--orange) 480px, #fbc934 760px, var(--yellow) 1200px);
    font-family: "Overlock", sans-serif;
  }
  .header {
    position: absolute; left: 0; top: 0; width: 816px; height: 412px;
    background: radial-gradient(ellipse 420px 260px at 420px 210px, var(--glow) 0%, #33206f 55%, var(--navy) 100%);
  }
  .product-name {
    position: absolute; left: 0; top: 130px; width: 816px;
    text-align: center;
    font-family: "Fredoka", sans-serif;
    font-weight: 700;
    color: var(--orange);
    font-size: 92px;
    line-height: 1.0;
  }
  .tagline-band {
    position: absolute; left: 0; top: 412px; width: 816px; height: 76px;
    background: var(--green);
    border-top: 12px solid var(--purple);
    border-bottom: 10px solid var(--purple);
    box-shadow: 0 8px 10px rgba(120, 60, 20, 0.35);
    display: flex; align-items: center; justify-content: center;
  }
  .tagline {
    font-family: "Fredoka", sans-serif;
    font-weight: 600;
    color: var(--white);
    font-size: 35px;
    letter-spacing: 0.6px;
  }
  .benefits { position: absolute; left: 78px; top: 540px; list-style: none; }
  .benefit {
    display: flex; align-items: center;
    height: 76.5px;
    font-size: 27px;
    font-weight: 700;
    color: var(--ink);
    line-height: 1.28;
  }
  .benefit-icon {
    flex: none;
    width: 68px; height: 68px;
    border-radius: 50%;
    background: var(--purple);
    border: 3px solid var(--white);
    box-shadow: 0 0 0 2px var(--purple);
    margin-right: 20px;
    display: flex; align-items: center; justify-content: center;
  }
  .benefit-icon svg { width: 40px; height: 40px; }
  .benefit--two-line { margin-top: 22px; }

  .contact-panel {
    position: absolute; left: 52px; top: 1012px; width: 716px; height: 140px;
    background: var(--purple);
    border-radius: 28px;
    padding: 16px 0 0 64px;
    font-family: "Fredoka", sans-serif;
    font-weight: 700;
    color: var(--white);
  }
  .phone { font-size: 60px; line-height: 1.0; letter-spacing: 1px; }
  .website { font-size: 38px; line-height: 1.2; }

  .leaves {
    position: absolute; left: 640px; top: 826px; width: 135px; height: 215px;
    border-radius: 60% 40% 50% 50% / 55% 45% 55% 45%;
    background: linear-gradient(160deg, #22ad55, var(--green-dark));
  }
  .eco-badge {
    position: absolute; left: 484px; top: 907px; width: 196px; height: 128px;
    background: var(--green);
    border: 5px solid var(--white);
    outline: 3px solid var(--green-dark);
    border-radius: 6px;
    transform: rotate(-1deg);
    display: flex; flex-direction: column; align-items: center; justify-content: center;
    font-family: "Oswald", sans-serif;
    font-weight: 500;
    color: var(--white);
    line-height: 1.05;
  }
  .eco-badge .eco-small { font-size: 20px; }
  .eco-badge .eco-large { font-size: 38px; }
  .bug-character {
    position: absolute; left: 382px; top: 922px; width: 118px; height: 100px;
    border-radius: 50% 45% 40% 50%;
    background: radial-gradient(circle at 55% 55%, var(--bug-brown) 0%, #7a6054 55%, #9fd2ef 100%);
  }
</style>
</head>
<body>
<main class="sticker">
  <header class="header">
    <h1 class="product-name">The Swift<br>Bug Stick</h1>
  </header>

  <div class="tagline-band">
    <p class="tagline">Make Bugs Disappear With Just A Touch!</p>
  </div>

  <ul class="benefits">
    <li class="benefit">
      <span class="benefit-icon">
        <svg viewBox="0 0 40 40" fill="none" stroke="#fff" stroke-width="3" stroke-linejoin="round" stroke-linecap="round">
          <path d="M20 4 L33 9 V19 C33 27 27 33 20 36 C13 33 7 27 7 19 V9 Z"/>
          <path d="M13 20 L18 25 L27 15"/>
        </svg>
      </span>
      Instantly capture bugs from a safe distance
    </li>
    <li class="benefit">
      <span class="benefit-icon">
        <svg viewBox="0 0 40 40" fill="#fff" stroke="#fff" stroke-width="2" stroke-linecap="round">
          <ellipse cx="20" cy="23" rx="8" ry="11"/>
          <circle cx="20" cy="10" r="4"/>
          <path d="M12 18 L5 14 M12 24 L5 24 M12 30 L6 34 M28 18 L35 14 M28 24 L35 24 M28 30 L34 34" fill="none"/>
        </svg>
      </span>
      Works on any bug, from any angle
    </li>
    <li class="benefit">
      <span class="benefit-icon">
        <svg viewBox="0 0 40 40" fill="none" stroke="#fff" stroke-width="3" stroke-linecap="round">
          <rect x="13" y="10" width="14" height="22" rx="3"/>
          <path d="M16 6 H24"/>
          <circle cx="20" cy="20" r="16"/>
          <path d="M9 9 L31 31"/>
        </svg>
      </span>
      No dangerous chemicals
    </li>
    <li class="benefit">
      <span class="benefit-icon">
        <svg viewBox="0 0 40 40" fill="#fff">
          <path d="M22 4 C23 14 26 17 36 18 C26 19 23 22 22 32 C21 22 18 19 8 18 C18 17 21 14 22 4 Z"/>
          <path d="M9 24 C9.5 29 11 30.5 16 31 C11 31.5 9.5 33 9 38 C8.5 33 7 31.5 2 31 C7 30.5 8.5 29 9 24 Z"/>
        </svg>
      </span>
      No mess on shoes or walls
    </li>
    <li class="benefit benefit--two-line">
      <span class="benefit-icon">
        <svg viewBox="0 0 40 40" fill="#fff">
          <rect x="6" y="17" width="7" height="17" rx="1.5"/>
          <path d="M15 18 L21 6 C24 6 25 8 24 12 L23 16 H32 C34 16 35 18 34.5 20 L32 31 C31.5 33 30 34 28 34 H15 Z"/>
        </svg>
      </span>
      You choose to save or<br>kill the bug (usually)
    </li>
  </ul>

  <footer class="contact-panel">
    <p class="phone">0198765432</p>
    <p class="website">www.theswiftbugstick.com</p>
  </footer>

  <div class="leaves" role="img" aria-label="Illustration of two green leaves"></div>
  <div class="eco-badge">
    <span class="eco-small">ENVIRONMENTALLY</span>
    <span class="eco-large">FRIENDLY!</span>
  </div>
  <div class="bug-character" role="img" aria-label="Cartoon bug character peeking over the sign"></div>
</main>
</body>
</html>
```